"Velvet Haven" Mattress Pad Packaging

We need packaging for a mattress pad. This will be sold through retailers across North America. We need something modern and clean, an update from what we currently have. This is targeted towards older women. I've attached what our current packaging looks like as well as other mattress pad packaging. This is a simple product so we're open to creativity and experimentation. This is our first time using this site so we're very open and hoping for something fun.

Font styles to use
Serif
Sans Serif

Colors

Designer to choose colors to be used in the design.

```html
<!DOCTYPE html>
<html lang="en">
<head>
<meta charset="utf-8">
<title>Velvet Haven Mattress Pad Packaging</title>
<link href="https://fonts.googleapis.com/css2?family=Cinzel:wght@400;500&family=Tinos:wght@400;700&display=swap" rel="stylesheet">
<style>
  :root {
    --ink: #000000;
    --divider: #ffffff;
    --gold-light: #dbb877;
    --gold-mid: #c8a15c;
    --gold-deep: #b88a3f;
    --silver-light: #e6e6e6;
    --silver-mid: #c4c4c4;
    --silver-deep: #8f8f8f;
  }
  * { margin: 0; padding: 0; box-sizing: border-box; }
  html, body {
    width: 1200px;
    height: 2684px;
    overflow: hidden;
    background: var(--divider);
  }
  .canvas {
    position: relative;
    width: 1200px;
    height: 2684px;
  }
  .panel {
    position: absolute;
    left: 0;
    width: 1200px;
    height: 1339px;
    background: var(--ink);
    overflow: hidden;
  }
  .panel--gold {
    top: 0;
    height: 1337px;
    --light: var(--gold-light);
    --mid: var(--gold-mid);
    --deep: var(--gold-deep);
  }
  .panel--silver {
    top: 1345px;
    --light: var(--silver-light);
    --mid: var(--silver-mid);
    --deep: var(--silver-deep);
  }
  .panel__texture {
    position: absolute;
    inset: 0;
    background: radial-gradient(ellipse at 50% 45%, #0d0c0b 0%, #000 70%);
  }
  .frame {
    position: absolute;
    left: 41px;
    top: 41px;
    width: 1118px;
    height: 1256px;
    background: linear-gradient(100deg, var(--mid) 0%, var(--light) 22%, var(--deep) 45%, var(--light) 65%, var(--deep) 85%, var(--light) 100%);
  }
  .frame__inner {
    position: absolute;
    left: 18px;
    top: 18px;
    right: 18px;
    bottom: 18px;
    background: radial-gradient(ellipse at 50% 45%, #0d0c0b 0%, #000 70%);
  }
  .metal {
    background: linear-gradient(100deg, var(--mid) 0%, var(--light) 30%, var(--deep) 60%, var(--light) 100%);
    -webkit-background-clip: text;
    background-clip: text;
    color: transparent;
  }
  .line {
    position: absolute;
    left: 0;
    width: 1200px;
    text-align: center;
    white-space: nowrap;
  }
  .brand__mark {
    position: absolute;
    left: 522px;
    top: 120px;
    width: 156px;
    height: 156px;
    border: 4px solid var(--mid);
    border-radius: 50%;
  }
  .brand__name {
    top: 330px;
    font-family: "Cinzel", serif;
    font-weight: 400;
    font-size: 52px;
    letter-spacing: 5px;
    color: var(--mid);
  }
  .title {
    font-family: "Cinzel", serif;
    font-weight: 400;
    line-height: 1;
  }
  .title--mattress {
    top: 492px;
    font-size: 162px;
    letter-spacing: -2px;
  }
  .title--pad {
    top: 710px;
    font-size: 162px;
  }
  .subtitle {
    top: 660px;
    font-family: "Tinos", serif;
    font-size: 38px;
    letter-spacing: 30px;
    padding-left: 30px;
    line-height: 1;
  }
  .features {
    position: absolute;
    top: 918px;
    left: 0;
    width: 1200px;
    list-style: none;
    text-align: center;
    font-family: "Tinos", serif;
    font-size: 32px;
    line-height: 40px;
  }
  .features li { display: block; }
  .features li span { display: inline-block; }
  .size {
    top: 1188px;
    font-family: "Tinos", serif;
    font-weight: 700;
    font-size: 46px;
    line-height: 1;
  }
</style>
</head>
<body>
<main class="canvas">
  <section class="panel panel--gold" aria-label="Gold edition label">
    <div class="panel__texture" role="img" aria-label="Faint gold wood-grain line pattern"></div>
    <div class="frame"><div class="frame__inner" role="img" aria-label="Faint gold wood-grain line pattern"></div></div>
    <div class="brand__mark"></div>
    <p class="line brand__name">VELVET HAVEN</p>
    <h1 class="line title title--mattress"><span class="metal">MATTRESS</span></h1>
    <p class="line subtitle"><span class="metal">LUXURY QUILTED</span></p>
    <p class="line title title--pad"><span class="metal">PAD</span></p>
    <ul class="features">
      <li><span class="metal">300 THREAD COUNT</span></li>
      <li><span class="metal">STRETCH-TO-FIT-SKIRT</span></li>
      <li><span class="metal">ALLERGY DETERRENT</span></li>
      <li><span class="metal">100% COTTON</span></li>
    </ul>
    <p class="line size"><span class="metal">QUEEN</span></p>
  </section>

  <section class="panel panel--silver" aria-label="Silver edition label">
    <div class="panel__texture" role="img" aria-label="Faint silver wood-grain line pattern"></div>
    <div class="frame"><div class="frame__inner" role="img" aria-label="Faint silver wood-grain line pattern"></div></div>
    <div class="brand__mark"></div>
    <p class="line brand__name">VELVET HAVEN</p>
    <h2 class="line title title--mattress"><span class="metal">MATTRESS</span></h2>
    <p class="line subtitle"><span class="metal">LUXURY QUILTED</span></p>
    <p class="line title title--pad"><span class="metal">PAD</span></p>
    <ul class="features">
      <li><span class="metal">300 THREAD COUNT</span></li>
      <li><span class="metal">STRETCH-TO-FIT-SKIRT</span></li>
      <li><span class="metal">ALLERGY DETERRENT</span></li>
      <li><span class="metal">100% COTTON</span></li>
    </ul>
    <p class="line size"><span class="metal">QUEEN</span></p>
  </section>
</main>
</body>
</html>
```